I work in the manufacturing industry and currently for TK in the wind department. I'm a contractor. So no TK symbol can be on the card but I can put a wind turbine on it. I am a skydiver as well, so I want a skydiver in the parachute floating next to a turbine with some clouds, the sun over head and the ground below. Hits the moto.

Quality inspection and manufacturing is the industry I work in.

Industry

Walter Denshaw
PXR (manufacturing Quality Inspector)
"Analyzing Quality from a different angle!"

Lark48213@mailbox-example.com
555-302-7184

• Skydiver in parachute, wind turbine, clouds, the sun and the ground. If you can come up with a better moto, please let me know. The back side display "FenLatch inc" in small text in a corner.

```html
<!DOCTYPE html>
<html lang="en">
<head>
<meta charset="utf-8">
<title>Walter Denshaw – Business Card Back</title>
<link rel="stylesheet" href="https://fonts.googleapis.com/css2?family=Audiowide&display=swap">
<style>
  :root {
    --sky-light: #eaf9fd;
    --sky-mid: #c9f0fa;
    --sky-deep: #b3e6f5;
    --text-yellow: #ffe11c;
    --text-outline: #2b2108;
    --text-shadow: rgba(40, 40, 40, 0.55);
    --company-blue: #a9dcff;
    --company-outline: #3f83c4;
  }
  html, body {
    margin: 0;
    padding: 0;
    overflow: hidden;
    background: #ffffff;
  }
  .card {
    position: relative;
    width: 1200px;
    height: 702px;
    overflow: hidden;
    font-family: "Audiowide", sans-serif;
  }
  .sky-backdrop {
    position: absolute;
    inset: 0;
    background:
      radial-gradient(ellipse 40% 25% at 25% 20%, rgba(255,255,255,0.55), transparent 70%),
      radial-gradient(ellipse 35% 22% at 75% 15%, rgba(255,255,255,0.5), transparent 70%),
      radial-gradient(ellipse 45% 25% at 70% 80%, rgba(255,255,255,0.5), transparent 70%),
      radial-gradient(ellipse 40% 22% at 15% 85%, rgba(255,255,255,0.45), transparent 70%),
      linear-gradient(180deg, var(--sky-mid) 0%, var(--sky-light) 50%, var(--sky-deep) 100%);
  }
  .contact-block {
    position: absolute;
    left: 0;
    right: 0;
    top: 0;
    text-align: center;
  }
  .contact-line {
    position: absolute;
    left: 0;
    right: 0;
    margin: 0;
    font-size: 38px;
    line-height: 1;
    color: var(--text-yellow);
    -webkit-text-stroke: 3px var(--text-outline);
    paint-order: stroke fill;
    text-shadow: 4px 4px 4px var(--text-shadow);
    white-space: nowrap;
  }
  .contact-name { top: 202px; }
  .contact-title { top: 260px; }
  .contact-email { top: 368px; }
  .contact-phone { top: 481px; }
  .company-name {
    position: absolute;
    right: 72px;
    top: 610px;
    margin: 0;
    font-size: 36px;
    line-height: 1;
    color: var(--company-blue);
    -webkit-text-stroke: 3px var(--company-outline);
    paint-order: stroke fill;
    white-space: nowrap;
  }
</style>
</head>
<body>
  <main class="card">
    <div class="sky-backdrop" role="img" aria-label="Soft blue sky with drifting white clouds"></div>
    <section class="contact-block">
      <p class="contact-line contact-name">Contact: Walter Denshaw</p>
      <p class="contact-line contact-title">PXR (manufacturing Quality Inspector)</p>
      <p class="contact-line contact-email">Email: Lark48213@mailbox-example.com</p>
      <p class="contact-line contact-phone">Phone: 555-302-7184</p>
    </section>
    <p class="company-name">FenLatch, Inc.</p>
  </main>
</body>
</html>
```